**** Business card design for VoltaNode ****

For my ICT company VoltaNode I need I need a business card design.

We design, build and host web-applications and we have our own CMS product.

Some good examples are attached.

The information should be:
Joris Tielenburg
Managing director
E: j.tielenburg@voltanode-example.nl
M: +31(0)6 57218064
T: +31(0)40 7249305
W: www.voltanode-example.nl

Address:
Berend Vlootweg 27
5612 KT Eindhoven

Industry/Entity Type

Business

Requirements
Must have
• - Use logo (see attachments)
- Double sided
- Distinctive
Nice to have
• - Place for a statement on the back-side: "Designed with knowledge, built with passion"
- HTML code (or Wordpress)
- Dark (black or dark-gray) side
- Small simple images for telephone, e-mail en Url.
- QR code (only if not disturbing), not required, just an option

```html
<!DOCTYPE html>
<html lang="en">
<head>
<meta charset="utf-8">
<title>VoltaNode – Business card</title>
<link rel="stylesheet" href="https://fonts.googleapis.com/css2?family=Jura:wght@400;500;600&display=swap">
<style>
  :root {
    --stage: #2a2c2f;
    --card-white: #ffffff;
    --band-dark: #3e4144;
    --band-top: #383b3e;
    --name-blue: #1a8fd6;
    --ink: #1e1f21;
    --brand-grey: #4a6a76;
    --band-text: #f2f4f5;
    --art-light: #5fc3f2;
    --art-mid: #2a7fd0;
    --art-deep: #1d3f9c;
  }
  * { box-sizing: border-box; margin: 0; padding: 0; }
  html, body {
    width: 1200px; height: 799px; overflow: hidden;
    background: var(--stage);
    font-family: "Jura", sans-serif;
  }
  .card {
    position: absolute; left: 75px; top: 100px;
    width: 1050px; height: 600px;
    background: var(--card-white);
    overflow: hidden;
  }
  .card__top-band {
    position: absolute; left: 0; top: 0; width: 100%; height: 16px;
    background: var(--band-top);
  }
  .card__bottom-band {
    position: absolute; left: 0; bottom: 0; width: 100%; height: 79px;
    background: var(--band-dark);
  }
  .card__artwork {
    position: absolute; left: 0; top: 0; width: 1050px; height: 600px;
  }
  .brand {
    position: absolute; left: 40px; top: 44px;
    display: flex; align-items: center; gap: 26px;
  }
  .brand__dot {
    width: 118px; height: 118px; border-radius: 50%;
    background: var(--art-mid);
  }
  .brand__name {
    font-size: 52px; font-weight: 500; letter-spacing: 1px;
    color: var(--brand-grey);
  }
  .person {
    position: absolute; left: 39px; top: 278px;
  }
  .person__name {
    font-size: 28px; font-weight: 600; color: var(--name-blue); line-height: 1.05;
  }
  .person__role {
    font-size: 23px; font-weight: 500; color: var(--ink); line-height: 1.1;
  }
  .address {
    position: absolute; left: 39px; top: 474px;
    font-size: 21px; font-weight: 500; color: var(--ink);
  }
  .contact {
    position: absolute; top: 532px;
    font-size: 19px; font-weight: 500; color: var(--band-text);
    line-height: 28px;
  }
  .contact--personal { left: 39px; }
  .contact--company { left: 532px; }
</style>
</head>
<body>
  <main class="card">
    <div class="card__top-band"></div>
    <div class="card__bottom-band"></div>

    <svg class="card__artwork" viewBox="0 0 1050 600" role="img"
         aria-label="Large blue three-dimensional brand artwork with circling arrows around a silver sphere">
      <defs>
        <radialGradient id="artGlow" cx="0.55" cy="0.5" r="0.65">
          <stop offset="0" stop-color="var(--art-light)"/>
          <stop offset="0.55" stop-color="var(--art-mid)"/>
          <stop offset="1" stop-color="var(--art-deep)"/>
        </radialGradient>
      </defs>
      <path d="M1050 16 L740 16 C640 120 600 260 640 380 C680 470 740 520 820 600 L1050 600 Z"
            fill="url(#artGlow)" opacity="0.9"/>
    </svg>

    <div class="brand">
      <span class="brand__dot"></span>
      <span class="brand__name">VoltaNode</span>
    </div>

    <div class="person">
      <p class="person__name">Joris Tielenburg</p>
      <p class="person__role">Managing director</p>
    </div>

    <p class="address">Berend Vlootweg 27. 5612 KT Eindhoven</p>

    <div class="contact contact--personal">
      <p>E: j.tielenburg@voltanode-example.nl</p>
      <p>M: +31(0)6 57218064</p>
    </div>
    <div class="contact contact--company">
      <p>T: +31(0)40 7249305</p>
      <p>W: www.voltanode-example.nl</p>
    </div>
  </main>
</body>
</html>
```